Design a website for a new innovative shipping service

Parcivo.com is a new business concept that makes it easy and inexpensive for private individuals to ship packages to friends and families abroad. It is basically a website where customers can create and print shipping labels that they can put on their package and then drop off the package at any postal office.

We need an initial site design for the launch of the concept. The site is fairly simple – see the design brief and wireframes - both uploadet

We expect design of the entire label creation flow as well as basic content pages.

Target Market(s)

See design brief

Industry/Entity Type

Business

Number of Pages Required

5+ page

Requirements
Must have
• See design brief
Nice to have
• See design brief
Should not have
• See design brief

```html
<!DOCTYPE html>
<html lang="en">
<head>
<meta charset="utf-8">
<title>Parcivo – Send it home</title>
<link rel="stylesheet" href="https://fonts.googleapis.com/css2?family=Open+Sans:wght@400;600;700&display=swap">
<style>
  :root {
    --orange: #f47a20;
    --orange-dark: #e0661a;
    --navy: #1f3046;
    --navy-deep: #172538;
    --ink: #26374f;
    --grey: #8c929b;
    --white: #ffffff;
    --field: #f4f4f4;
  }
  * { box-sizing: border-box; margin: 0; padding: 0; }
  html, body { width: 893px; height: 1200px; overflow: hidden; }
  body { font-family: "Open Sans", Arial, sans-serif; background: var(--white); position: relative; }

  .hero { position: absolute; left: 0; top: 0; width: 893px; height: 425px; overflow: hidden; }
  .hero-photo { position: absolute; inset: 0;
    background: linear-gradient(100deg, #5b4a3f 0%, #8a6e58 30%, #6c6660 55%, #3f4c63 80%, #2b3a52 100%); }
  .hero-shade { position: absolute; inset: 0; background: rgba(20,28,40,0.28); }
  .brand { position: absolute; left: 34px; top: 18px; display: flex; align-items: center; gap: 8px;
    color: var(--white); font-weight: 600; font-size: 22px; }
  .brand-mark { width: 26px; height: 26px; background: var(--orange); }
  .lang { position: absolute; left: 740px; top: 28px; width: 34px; height: 18px; border: 1px solid rgba(255,255,255,0.7);
    color: var(--white); font-size: 10px; text-align: center; line-height: 16px; }
  .social { position: absolute; right: 0; top: 138px; display: flex; flex-direction: column; gap: 3px; }
  .social span { display: block; width: 20px; height: 20px; background: rgba(255,255,255,0.55); }
  .hero-title { position: absolute; left: 0; top: 128px; width: 100%; text-align: center; color: var(--white);
    font-size: 42px; font-weight: 700; letter-spacing: 1px; }
  .hero-sub { position: absolute; left: 0; top: 200px; width: 100%; text-align: center; color: var(--white);
    font-size: 22px; font-weight: 600; }
  .btn-how { position: absolute; left: 388px; top: 277px; width: 114px; height: 40px; background: var(--orange);
    color: var(--white); font-size: 16px; line-height: 40px; text-align: center; }
  .hero-badge { position: absolute; left: 428px; top: 392px; width: 38px; height: 38px; border-radius: 50%;
    background: var(--navy); z-index: 2; }

  .quote-bar { position: absolute; left: 0; top: 425px; width: 893px; height: 86px; background: var(--navy); }
  .field { position: absolute; top: 26px; height: 32px; background: var(--field); color: #666; font-size: 11px;
    line-height: 32px; padding-left: 10px; }
  .field-from { left: 119px; width: 246px; }
  .field-to { left: 378px; width: 243px; }
  .field-to .caret { position: absolute; right: 0; top: 0; width: 30px; height: 32px; background: var(--orange);
    display: flex; align-items: center; justify-content: center; }
  .btn-prices { position: absolute; left: 631px; top: 26px; width: 138px; height: 32px; background: #0d0f12;
    border: 1px solid #555; color: var(--white); font-size: 12px; font-weight: 700; text-align: center; line-height: 30px; }

  .ship { position: absolute; left: 0; top: 511px; width: 893px; height: 382px; text-align: center; }
  .ship h2 { margin-top: 24px; font-size: 31px; font-weight: 600; color: var(--ink); }
  .ship .lead { width: 560px; margin: 30px auto 0; font-size: 11px; line-height: 15px; color: var(--grey); }
  .ship .accent { margin-top: 8px; font-size: 18px; font-weight: 700; color: var(--orange); }
  .items { position: absolute; top: 178px; left: 135px; display: flex; gap: 18px; align-items: flex-end; }
  .item { height: 170px; border-radius: 6px; }
  .item-books { width: 140px; background: linear-gradient(180deg, #5fb0d8, #e2574c 45%, #f0c23a 75%, #8ac04a); }
  .item-statue { width: 120px; background: linear-gradient(180deg, #7a5a3e, #4a3424); }
  .item-gift { width: 150px; background: linear-gradient(180deg, #3a8ad8 0%, #f08a24 40%, #f58c1f 100%); }
  .item-shoes { width: 150px; height: 110px; background: linear-gradient(180deg, #c23232, #2a2a2a); }

  .trust { position: absolute; left: 0; top: 893px; width: 893px; height: 262px; background: var(--orange); }
  .trust h2 { margin-top: 18px; text-align: center; color: var(--white); font-size: 25px; font-weight: 600; }
  .cards { position: absolute; left: 119px; top: 75px; display: flex; gap: 12px; }
  .card { position: relative; width: 321px; height: 140px; background: var(--white); padding: 26px 20px 0 110px; }
  .avatar { position: absolute; left: 22px; top: 30px; width: 74px; height: 74px; border-radius: 50%;
    background: linear-gradient(180deg, #d8b79a, #7e5a44); border: 3px solid #eee; }
  .card-text { font-size: 10px; line-height: 14px; color: #666; }
  .card-name { margin-top: 8px; font-size: 10px; font-weight: 700; color: var(--ink); }
  .card .q { position: absolute; font-size: 26px; color: #d6d6d6; font-weight: 700; line-height: 1; }
  .q-open { left: 100px; top: 6px; }
  .q-close { right: 12px; bottom: 4px; }
  .dots { position: absolute; top: 230px; left: 0; width: 100%; display: flex; justify-content: center; gap: 8px; }
  .dots span { width: 9px; height: 9px; border-radius: 50%; background: rgba(255,255,255,0.5); }
  .dots span.on { background: var(--white); }

  .footer { position: absolute; left: 0; top: 1155px; width: 893px; height: 45px; background: var(--navy-deep);
    color: #c9ced6; font-size: 11px; }
  .footer-nav { position: absolute; left: 124px; top: 15px; display: flex; gap: 26px; }
  .footer-mark { position: absolute; left: 437px; top: 13px; width: 18px; height: 18px; background: var(--orange); }
  .copyright { position: absolute; right: 122px; top: 15px; }
</style>
</head>
<body>

<header class="hero">
  <div class="hero-photo" role="img" aria-label="Photo of a smiling woman receiving a cardboard parcel from a courier"></div>
  <div class="hero-shade"></div>
  <div class="brand"><span class="brand-mark"></span>parcivo</div>
  <div class="lang">EN</div>
  <div class="social"><span></span><span></span><span></span><span></span><span></span><span></span></div>
  <h1 class="hero-title">SEND IT HOME</h1>
  <p class="hero-sub">Send parcels to your home at lowest rates</p>
  <div class="btn-how">How It Works</div>
  <div class="hero-badge"></div>
</header>

<section class="quote-bar">
  <div class="field field-from">Choose Sender Location</div>
  <div class="field field-to">Choose Recipient Location
    <span class="caret"><svg width="10" height="6" viewBox="0 0 10 6"><path d="M0 0 L10 0 L5 6 Z" fill="#fff"/></svg></span>
  </div>
  <div class="btn-prices">Click to see prices</div>
</section>

<section class="ship">
  <h2>What do you want to ship?</h2>
  <p class="lead">No matter who you are – an individual or business you would like to spend less time &amp; money on sending things to anywhere you want. We are here to help you.</p>
  <p class="accent">THAT CAN BE ANYTHING</p>
  <div class="items">
    <div class="item item-books" role="img" aria-label="Stack of colourful books"></div>
    <div class="item item-statue" role="img" aria-label="Small seated bronze statue"></div>
    <div class="item item-gift" role="img" aria-label="Orange gift box with blue ribbon"></div>
    <div class="item item-shoes" role="img" aria-label="Pair of red sneakers"></div>
  </div>
</section>

<section class="trust">
  <h2>Your trust means everything for us</h2>
  <div class="cards">
    <article class="card">
      <span class="q q-open">“</span>
      <div class="avatar" role="img" aria-label="Customer portrait"></div>
      <p class="card-text">I used Parcivo for the first time 2 weeks ago and it was very easy. The parcel sent via the site reached my daughter in Chengdu after only 3 days.</p>
      <p class="card-name">Anna Wu, Beijing</p>
      <span class="q q-close">”</span>
    </article>
    <article class="card">
      <span class="q q-open">“</span>
      <div class="avatar" role="img" aria-label="Customer portrait"></div>
      <p class="card-text">I used Parcivo for the first time 2 weeks ago and it was very easy. The parcel sent via the site reached my daughter in Chengdu after only 3 days.</p>
      <p class="card-name">Lina Chen, Beijing</p>
      <span class="q q-close">”</span>
    </article>
  </div>
  <div class="dots"><span class="on"></span><span></span><span></span></div>
</section>

<footer class="footer">
  <nav class="footer-nav"><span>About</span><span>Terms</span><span>Help</span></nav>
  <span class="footer-mark"></span>
  <span class="copyright">Copyright©2015 Parcivo</span>
</footer>

</body>
</html>
```